Birchford Realty Business Card

Business Card:

Somewhere on front of card, please include Broker License Number: 5839162

Website is BirchfordRealty.example

Address is:
7218 Crestover Ave E
Saginaw, MI 48271

I'll let you use creative freedom on the rest; we obviously need Name, Title, Email (@BirchfordRealty.example), Office Phone, Cell Phone.

Don't want any special die-cutting, just a standard size business card.

On the back, include a place for the date and time of an appointment to be written in pen.

Requirements
Must have
• Our logo, attached to email.

```html
<!DOCTYPE html>
<html lang="en">
<head>
<meta charset="utf-8">
<title>Birchford Realty Business Card</title>
<link href="https://fonts.googleapis.com/css2?family=Ubuntu:wght@500;700&family=Didact+Gothic&display=swap" rel="stylesheet">
<style>
  :root {
    --navy: #2a2865;
    --grey: #a3a3a3;
    --heading: #b4b4c2;
    --paper: #f4f4f4;
    --ink: #333338;
    --backdrop: #1c1c1e;
  }
  * { box-sizing: border-box; margin: 0; padding: 0; }
  html, body { width: 1200px; height: 1001px; overflow: hidden; background: var(--backdrop); }
  body { position: relative; font-family: "Didact Gothic", sans-serif; color: var(--ink); }

  .card { position: absolute; left: 306px; width: 589px; height: 330px; background: var(--paper); overflow: hidden; }
  .card--front { top: 133px; }
  .card--back { top: 539px; }

  /* Front */
  .brand { position: absolute; font-family: "Ubuntu", sans-serif; font-weight: 700; color: var(--navy); line-height: 1; text-align: right; white-space: nowrap; }
  .card--front .brand { right: 331px; top: 138px; font-size: 44px; }
  .brand span { display: block; font-size: 0.56em; margin-top: 3px; }
  .divider { position: absolute; left: 296px; top: 72px; width: 1px; height: 184px; background: #c9c9c9; }
  .holder { position: absolute; left: 333px; top: 77px; }
  .holder__name { font-family: "Ubuntu", sans-serif; font-weight: 700; font-size: 20px; color: var(--navy); letter-spacing: 0.3px; line-height: 1.1; }
  .holder__title { font-size: 15px; margin-top: 1px; }
  .contacts { list-style: none; position: absolute; left: 333px; top: 130px; font-size: 15px; }
  .contacts li { display: flex; align-items: center; height: 17.6px; }
  .contacts svg { width: 14px; height: 14px; margin-right: 10px; flex: none; }
  .address { position: absolute; left: 332px; top: 212px; font-size: 15px; line-height: 18px; font-style: normal; }
  .license { position: absolute; left: 332px; top: 254px; font-size: 12.5px; color: var(--navy); }
  .front-band { position: absolute; left: 0; bottom: 0; width: 589px; height: 19px; }

  /* Back */
  .back-top { position: absolute; left: 0; top: 0; width: 100%; height: 138px; background: var(--navy); }
  .back-heading { position: absolute; left: 35px; top: 66px; font-family: "Ubuntu", sans-serif; font-weight: 700; font-size: 20px; color: var(--heading); letter-spacing: 0.2px; padding-bottom: 8px; border-bottom: 1px solid #55548a; line-height: 1.1; }
  .card--back .brand { right: 42px; top: 56px; font-size: 44px; color: #ffffff; }
  .fields { position: absolute; left: 33px; right: 41px; top: 171px; font-size: 18px; color: #555; }
  .field { display: flex; align-items: flex-end; height: 26px; }
  .field + .field { margin-top: 30px; }
  .blank { border-bottom: 1px solid #555; height: 18px; margin-left: 6px; }
  .blank--grow { flex: 1; }
  .slash { margin: 0 2px; }
  .back-bottom { position: absolute; left: 0; bottom: 0; width: 100%; height: 54px; background: var(--navy); color: #ffffff; font-size: 15px; padding: 17px 0 0 33px; white-space: nowrap; }
</style>
</head>
<body>

<section class="card card--front">
  <div class="brand">Birchford<span>Realty</span></div>
  <div class="divider"></div>
  <div class="holder">
    <div class="holder__name">MORGAN HALE</div>
    <div class="holder__title">General Manager</div>
  </div>
  <ul class="contacts">
    <li><svg viewBox="0 0 14 14"><rect width="14" height="14" rx="2" fill="#2a2865"/><rect x="4.5" y="2.5" width="5" height="9" rx="1" fill="none" stroke="#fff" stroke-width="1.3"/></svg>989-555-0147</li>
    <li><svg viewBox="0 0 14 14"><rect width="14" height="14" rx="2" fill="#2a2865"/><path d="M4 3.5c0 4 2.5 6.5 6.5 6.5l.5-2-2-.8-.8 1C6.9 7.6 6.4 7.1 5.8 5.8l1-.8L6 3z" fill="#fff"/></svg>989-555-0146</li>
    <li><svg viewBox="0 0 14 14"><rect width="14" height="14" rx="2" fill="#2a2865"/><rect x="3" y="4.5" width="8" height="5.5" fill="none" stroke="#fff" stroke-width="1.1"/><path d="M3 4.5l4 3 4-3" fill="none" stroke="#fff" stroke-width="1.1"/></svg>info@BirchfordRealty.example</li>
    <li><svg viewBox="0 0 14 14"><rect width="14" height="14" rx="2" fill="#2a2865"/><circle cx="7" cy="7" r="4" fill="none" stroke="#fff" stroke-width="1"/><ellipse cx="7" cy="7" rx="1.7" ry="4" fill="none" stroke="#fff" stroke-width="0.9"/><path d="M3 7h8" stroke="#fff" stroke-width="0.9"/></svg>www.BirchfordRealty.example</li>
  </ul>
  <address class="address">7218 Crestover Ave E<br>Saginaw, MI 48271</address>
  <div class="license">Broker License #5839162</div>
  <svg class="front-band" viewBox="0 0 589 19" preserveAspectRatio="none">
    <polygon points="0,0 296,0 308,19 0,19" fill="#a3a3a3"/>
    <polygon points="296,0 589,0 589,19 308,19" fill="#2a2865"/>
  </svg>
</section>

<section class="card card--back">
  <div class="back-top"></div>
  <h2 class="back-heading">YOUR APPOINTMENTS</h2>
  <div class="brand">Birchford<span>Realty</span></div>
  <div class="fields">
    <div class="field">Name:<span class="blank blank--grow"></span></div>
    <div class="field">Date:<span class="blank" style="width:74px"></span><span class="slash">/</span><span class="blank" style="width:74px;margin-left:0"></span><span class="slash">/</span><span class="blank" style="width:74px;margin-left:0"></span><span style="margin-left:38px">Time:</span><span class="blank blank--grow" style="margin-left:12px"></span></div>
  </div>
  <div class="back-bottom">Please give us 48 hours notice if you will be unable to keep this appointment.</div>
</section>

</body>
</html>
```